Business Card Design

We have our logo and everything in place. Looking to have a layout for our new business cards designed. These will be printed with a matte finish, possibly rounded corners, and looking to incorporate some cool spot UV layers into the design.

Ive uploaded the existing card front and back as well as our logo.

Card Size Will Be 3.5" x 2"

Industry/Entity Type

Business

```html
<!DOCTYPE html>
<html lang="en">
<head>
<meta charset="utf-8">
<title>Cedarline Deck and Rail – Business Cards</title>
<link href="https://fonts.googleapis.com/css2?family=Noto+Serif:ital,wght@0,400;1,400&display=swap" rel="stylesheet">
<style>
  :root {
    --backdrop: #a9a7a7;
    --card: #2b2b2b;
    --ink: #ffffff;
    --ink-soft: #e6e6e6;
    --band-dark: #555252;
    --band-light: #a3a3a3;
  }
  * { margin: 0; padding: 0; box-sizing: border-box; }
  html, body {
    width: 1200px; height: 1200px; overflow: hidden;
    background: var(--backdrop);
    font-family: "Noto Serif", Georgia, serif;
    color: var(--ink);
  }
  .canvas { position: relative; width: 1200px; height: 1200px; }
  .card {
    position: absolute;
    width: 714px; height: 420px;
    background: var(--card);
    border-radius: 27px;
    overflow: hidden;
  }
  .card--front { left: 237px; top: 116px; }
  .card--back { left: 230px; top: 644px; }

  .brand-name {
    position: absolute;
    font-weight: 400;
    font-style: normal;
    color: var(--ink);
    text-align: center;
    line-height: 1.1;
    display: flex; align-items: center; justify-content: center; gap: 14px;
  }
  .brand-mark {
    width: 14px; height: 14px; background: var(--ink); flex: none;
  }
  .card--front .brand-name {
    left: 0; right: 0; top: 0; bottom: 0;
    font-size: 44px;
  }
  .card--back .brand-name {
    left: 30px; top: 175px; width: 310px;
    font-size: 26px;
  }

  .contact { position: absolute; left: 372px; top: 130px; }
  .contact__name { font-size: 32px; letter-spacing: 1px; line-height: 1.2; }
  .contact__title { font-size: 16px; font-style: italic; margin-top: 2px; color: var(--ink-soft); }
  .contact__list { list-style: none; margin-top: 20px; font-size: 17px; }
  .contact__list li { display: flex; align-items: center; height: 29px; }
  .contact__icon { width: 18px; height: 14px; margin-right: 17px; margin-left: 8px; fill: var(--ink); }

  .footer-band { position: absolute; left: 0; top: 0; }
  .website {
    position: absolute; left: 372px; top: 374px;
    font-size: 16px; letter-spacing: 0.3px; color: var(--ink-soft);
  }
</style>
</head>
<body>
<main class="canvas">
  <section class="card card--front" aria-label="Card front">
    <div class="brand-name"><span class="brand-mark"></span>Cedarline Deck and Rail</div>
  </section>

  <section class="card card--back" aria-label="Card back">
    <div class="brand-name"><span class="brand-mark"></span>Cedarline Deck and Rail</div>

    <div class="contact">
      <div class="contact__name">Daniel Mercer</div>
      <div class="contact__title">President</div>
      <ul class="contact__list">
        <li>
          <svg class="contact__icon" viewBox="0 0 18 14" aria-hidden="true">
            <path d="M1 5 Q9 -1 17 5 L15 7 L12 5.5 L12 4 Q9 3 6 4 L6 5.5 L3 7 Z"/>
            <path d="M4 8 L14 8 L16 13 L2 13 Z"/>
          </svg>403.555.0187
        </li>
        <li>
          <svg class="contact__icon" viewBox="0 0 18 14" aria-hidden="true">
            <path d="M1 2 L17 2 L17 13 L1 13 Z M2 3 L9 8.5 L16 3 Z" fill-rule="evenodd"/>
          </svg>cedarlinedeckandrail@mail.com
        </li>
      </ul>
    </div>

    <svg class="footer-band" width="714" height="420" viewBox="0 0 714 420" aria-hidden="true">
      <polygon points="346,365 714,365 714,420 310,420" fill="var(--band-dark)"/>
      <polygon points="0,392 328,392 310,420 0,420" fill="var(--band-light)"/>
    </svg>
    <div class="website">www.cedarlinedeckandrail.com</div>
  </section>
</main>
</body>
</html>
```